BrickaFun Business Card

We need a business card design for our company. We sell construction-themed amusement rides for kids.

Contact Information for Business Card

Contact info on business card should include:
Dale Hurst
Co-Founder & COO
(833) 517-BRICKAF
Dale@brickafun.com
www.brickafun.com

```html
<!DOCTYPE html>
<html lang="en">
<head>
<meta charset="utf-8">
<title>BrickaFun Business Card</title>
<link href="https://fonts.googleapis.com/css2?family=Russo+One&family=Exo+2:wght@400;500&display=swap" rel="stylesheet">
<style>
  :root{
    --stage:#1c1c1e;
    --card-white:#f4f4f4;
    --card-black:#232323;
    --band-gold:#c48a2c;
    --band-blue:#3aa9d8;
    --band-orange:#e8702e;
    --brand-orange:#e8702e;
    --text-light:#f2f2f2;
    --icon-blue:#3aa9d8;
    --icon-pink:#e0288a;
    --icon-purple:#7c3f9c;
    --art-hat:#f3c32a;
    --art-skin:#e9b48f;
  }
  *{margin:0;padding:0;box-sizing:border-box}
  html,body{width:1200px;height:900px;overflow:hidden;background:var(--stage)}
  .canvas{position:relative;width:1200px;height:900px;display:flex;align-items:center;justify-content:center}
  .card{position:relative;width:1050px;height:600px;border-radius:44px;overflow:hidden;background:var(--card-white)}
  .card-bands{position:absolute;inset:0;width:100%;height:100%}
  .brand{position:absolute;left:90px;top:90px;display:flex;align-items:center;gap:22px}
  .brand-dot{width:64px;height:64px;border-radius:50%;background:var(--brand-orange)}
  .brand-name{font-family:"Russo One",sans-serif;font-size:78px;color:var(--brand-orange);letter-spacing:1px}
  .person{position:absolute;left:60px;top:418px}
  .person-name{font-family:"Russo One",sans-serif;font-size:38px;color:var(--brand-orange);letter-spacing:2px;text-transform:uppercase}
  .person-title{font-family:"Exo 2",sans-serif;font-size:25px;color:var(--text-light);margin-top:4px;letter-spacing:1px}
  .crew-art{position:absolute;left:690px;top:200px;width:290px;height:250px;border-radius:20px;
    background:linear-gradient(160deg,var(--art-hat) 0%,var(--art-skin) 35%,var(--band-orange) 70%,#6b7c99 100%)}
  .contact{position:absolute;right:40px;top:468px;list-style:none;font-family:"Exo 2",sans-serif;font-size:25px;color:var(--text-light);letter-spacing:1px}
  .contact li{display:flex;align-items:center;justify-content:flex-end;gap:12px;height:36px}
  .contact svg{width:24px;height:24px;flex:none}
</style>
</head>
<body>
<main class="canvas">
  <article class="card">
    <svg class="card-bands" viewBox="0 0 1050 600" preserveAspectRatio="none" aria-hidden="true">
      <path d="M0 262 C260 330 560 420 1050 372 L1050 600 L0 600 Z" fill="var(--card-black)"/>
      <path d="M0 232 C280 300 560 395 1050 330 L1050 372 C560 420 260 330 0 262 Z" fill="var(--band-gold)"/>
      <path d="M0 214 C290 290 580 385 1050 305 L1050 322 C580 400 290 305 0 226 Z" fill="var(--band-blue)"/>
      <path d="M0 268 C270 336 560 428 1050 378 L1050 404 C560 448 270 350 0 280 Z" fill="var(--band-orange)"/>
      <path d="M0 288 C270 352 560 440 1050 410 L1050 414 C560 446 270 358 0 292 Z" fill="var(--text-light)"/>
    </svg>

    <div class="brand">
      <span class="brand-dot"></span>
      <span class="brand-name">BrickaFun</span>
    </div>

    <div class="person">
      <p class="person-name">Dale Hurst</p>
      <p class="person-title">Co-Founder &amp; COO</p>
    </div>

    <div class="crew-art" role="img" aria-label="Illustration of two cartoon construction workers in yellow hard hats"></div>

    <ul class="contact">
      <li>(833) 517-BRICKAF
        <svg viewBox="0 0 24 24"><circle cx="12" cy="12" r="12" fill="var(--icon-blue)"/><path d="M8 7h2l1 3-1.5 1a7 7 0 0 0 3.5 3.5l1-1.5 3 1v2a1 1 0 0 1-1 1A10 10 0 0 1 7 8a1 1 0 0 1 1-1z" fill="var(--card-black)"/></svg>
      </li>
      <li>Dale@brickafun.com
        <svg viewBox="0 0 24 24"><circle cx="12" cy="12" r="12" fill="var(--icon-pink)"/><rect x="6" y="8" width="12" height="8" rx="1" fill="none" stroke="var(--card-black)" stroke-width="1.6"/><path d="M6 8l6 5 6-5" fill="none" stroke="var(--card-black)" stroke-width="1.6"/></svg>
      </li>
      <li>www.brickafun.com
        <svg viewBox="0 0 24 24"><circle cx="12" cy="12" r="12" fill="var(--icon-purple)"/><circle cx="12" cy="12" r="6" fill="none" stroke="var(--card-black)" stroke-width="1.6"/><path d="M6 12h12M12 6c-3 3-3 9 0 12M12 6c3 3 3 9 0 12" fill="none" stroke="var(--card-black)" stroke-width="1.4"/></svg>
      </li>
    </ul>
  </article>
</main>
</body>
</html>
```